Book cover for a New Adult, romance/ contemporary novel.

I need a full front, back, and spine cover for my upcoming book. The novel is a romance/ coming of age book and is similar to Every Quiet Harbor by Marissa Colfax. My main audience is women in their late teens/ early 20's. The book is an emotional, reminiscent piece and I would love to see some cover designs with a darker palette like Waiting on Belmora, Nine Rooms Between, or Bartholomew and Kip (but I also adore some lighter covers, especially those that feature the couple such as A Different Then or Past Each Hour). Feel free to send some minimal designs as well if you have any! A great idea of that would be the cover for Salt and Clover or Waiting on Belmora. If you go with a minimal design, I'd love to see silhouettes or maybe a burning candle. Another possible idea I thought of would be a scene at a concert with the crowd silhouetted and then my main character (more details on her below) standing in the middle of it all. I prefer animation/drawing etc over real models. But feel free to send me whatever you think might match the vibe, I'd love to see anything you have in mind! Some main symbols in my book are stars and candles. The main character (Marisol) is a female Korean with brown, medium length straight hair, and the love interest (Theo) is a tall and thin male Caucasian with curly brown hair. The book is openly emotional, wistful, and sets an ache in your chest, so I can't wait to see what designs you artists come up with! (My barcode will need to be included on the back cover, and I am getting that soon!)
The title is "The Weight of Daylight" and the author's name is Brenna Quill. The book's dimensions will be 5.5x8.25. The blurb for the back cover is:
When happily ever falls apart, all you can do is move forward… and reminisce. Marisol Ahn returns home from college following a tragic incident she can’t bring herself to talk about and a breakup with her boyfriend, Theo Marsh. Finding it difficult to confront her traumas, she begins therapy. Marisol takes the therapist on a rollercoaster journey of her college life, retelling the events that caused her relationship to spiral out of control and led to her dropping out of pre-med despite that being her life-long dream. Marisol sets out to remember how things were before everything got so messed up, and figure out how to continue living now that they are.
The author bio for the back cover is:
Brenna Quill is the author of The Restless and Bold. She is a self published writer from Las Vegas who likes to pretend she’s currently in a New York bookstore, drinking a latte, while listening to a carefully curated playlist. When she’s not writing, Brenna is taking care of her plant babies and cuddling with the cutest puppy in the world.

```html
<!DOCTYPE html>
<html lang="en">
<head>
<meta charset="utf-8">
<title>The Weight of Daylight — Full Cover</title>
<link rel="stylesheet" href="https://fonts.googleapis.com/css2?family=Raleway:wght@700&family=Kalam:wght@300;400;700&family=Allura&display=swap">
<style>
  :root {
    --stage: #e4e4e4;
    --stage-edge: #d2d2d2;
    --cover: #000000;
    --ink: #ffffff;
    --accent: #2f97dc;
    --placeholder: #9b9b9b;
    --line-art: #1a1a1a;
  }
  * { box-sizing: border-box; margin: 0; padding: 0; }
  html, body { width: 1200px; height: 600px; overflow: hidden; }
  body {
    background: radial-gradient(ellipse at center, #f4f4f4 0%, var(--stage) 60%, var(--stage-edge) 100%);
    position: relative;
  }
  .cover-spread {
    position: absolute;
    left: 221px; top: 28px;
    width: 758px; height: 545px;
    background: var(--cover);
    overflow: hidden;
  }

  /* Back cover */
  .author-photo {
    position: absolute;
    left: 32px; top: 38px;
    width: 107px; height: 173px;
    background: var(--placeholder);
    display: flex; align-items: center; justify-content: center;
    overflow: hidden;
  }
  .author-photo span {
    font-family: Raleway, sans-serif;
    font-weight: 700;
    font-size: 34px;
    color: var(--ink);
    transform: rotate(-45deg);
  }
  .author-bio {
    position: absolute;
    left: 151px; top: 34px;
    width: 200px;
    font-family: Raleway, sans-serif;
    font-weight: 700;
    font-size: 12.2px;
    line-height: 15.1px;
    color: var(--ink);
    hyphens: auto;
  }
  .author-bio strong { font-size: 14.5px; }
  .divider {
    position: absolute;
    left: 29px; top: 229px;
    width: 321px; height: 3px;
    background: var(--accent);
  }
  .blurb {
    position: absolute;
    left: 32px; top: 250px;
    width: 310px;
    font-family: Kalam, cursive;
    font-weight: 300;
    font-size: 13.4px;
    line-height: 15.1px;
    color: var(--ink);
    text-indent: 16px;
    hyphens: auto;
  }

  /* Spine */
  .spine {
    position: absolute;
    left: 365px; top: 0;
    width: 31px; height: 545px;
  }
  .spine-author, .spine-title {
    position: absolute;
    left: 50%;
    writing-mode: vertical-rl;
    transform: translateX(-50%);
    color: var(--ink);
    white-space: nowrap;
  }
  .spine-author {
    top: 68px;
    font-family: Kalam, cursive;
    font-weight: 700;
    font-size: 15px;
    letter-spacing: 1px;
  }
  .spine-title {
    top: 240px;
    font-family: Kalam, cursive;
    font-weight: 400;
    font-size: 22px;
  }

  /* Front cover */
  .front {
    position: absolute;
    left: 396px; top: 0;
    width: 362px; height: 545px;
  }
  .front-art {
    position: absolute;
    inset: 90px 0 0 0;
    background: radial-gradient(ellipse at 30% 55%, var(--line-art) 0%, var(--cover) 70%);
  }
  .front-author {
    position: absolute;
    left: 62px; top: 30px;
    font-family: Kalam, cursive;
    font-weight: 400;
    font-size: 30px;
    letter-spacing: 4px;
    color: var(--ink);
    white-space: nowrap;
  }
  .front-title {
    position: absolute;
    left: 0; top: 0; width: 100%; height: 100%;
    font-family: Allura, cursive;
    color: var(--accent);
  }
  .front-title span { position: absolute; white-space: nowrap; line-height: 1; }
  .title-the { left: 20px; top: 370px; font-size: 40px; }
  .title-main { left: 68px; top: 335px; font-size: 96px; }
  .title-of { left: 112px; top: 445px; font-size: 24px; }
  .title-end { left: 132px; top: 418px; font-size: 64px; }
</style>
</head>
<body>
  <main class="cover-spread">
    <section class="back">
      <div class="author-photo" role="img" aria-label="Author photo placeholder"><span>Photo</span></div>
      <p class="author-bio"><strong>Brenna Quill</strong> is the author of The Restless and Bold. She is a self published writer from Las Vegas who likes to pretend she’s currently in a New York bookstore, drinking a latte, while listening to a carefully curated playlist. When she’s not writing, Brenna is taking care of her plant babies and cuddling with the cutest puppy in the world.</p>
      <div class="divider"></div>
      <p class="blurb">When happily ever falls apart, all you can do is move forward… and reminisce. Marisol Ahn returns home from college following a tragic incident she can’t bring herself to talk about and a breakup with her boyfriend, Theo Marsh. Finding it difficult to confront her traumas, she begins therapy. Marisol takes the therapist on a rollercoaster journey of her college life, retelling the events that caused her relationship to spiral out of control and led to her dropping out of pre-med despite that being her life-long dream. Marisol sets out to remember how things were before everything got so messed up, and figure out how to continue living now that they are.</p>
    </section>

    <section class="spine">
      <span class="spine-author">Brenna Quill</span>
      <span class="spine-title">The Weight of Daylight</span>
    </section>

    <section class="front">
      <div class="front-art" role="img" aria-label="White line drawing of a young woman and a young man in profile on black"></div>
      <p class="front-author">Brenna Quill</p>
      <h1 class="front-title" aria-label="The Weight of Daylight">
        <span class="title-the">the</span>
        <span class="title-main">weight</span>
        <span class="title-of">of</span>
        <span class="title-end">daylight</span>
      </h1>
    </section>
  </main>
</body>
</html>
```